Fun relaxed Travel Photography Business Card*

Require a fun, funky and quirky but rememberable business card for a travel photographer

Industry/Entity Type

Photographer

Contact Information for Business Card

Front Card

(my name) Dane M.

Travel Photographer ( small under travel photographer) “self-proclaimed”

(website logo) wanderingsofdane.example

(Snapgrid logo) @wanderings_of_dane

(Snapgrid logo) @wanderings_of_dane_2.0 (backup for when Snapgrid puts Dane on timeout for bad behaviour)

Tel: N/A (removing the potential awkwardness of me not replying)

Email: (see above)

Back Card

Offending people since 1986

(Bottom right corner) “p.s. travelling made me fatTER”

Font styles to use
Serif

Colors

Designer to choose colors to be used in the design.

Requirements
Must have
• a camera
• a similar cartoon version of me as the "logo" see attached files, try to make as similar as possible

```html
<!DOCTYPE html>
<html lang="en">
<head>
<meta charset="utf-8">
<title>Dane M. – Travel Photographer Business Card</title>
<link rel="stylesheet" href="https://fonts.googleapis.com/css2?family=Bubblegum+Sans&family=Oswald:wght@600&family=Gochi+Hand&family=Open+Sans:wght@400&family=Pompiere&family=Cormorant+SC:wght@500&family=Fredoka:wght@500&display=swap">
<style>
  :root {
    --backdrop: #c65b3e;
    --card-white: #f7f7f7;
    --card-grey: #dedede;
    --sun-yellow: #f2b83a;
    --sun-deep: #dfa02c;
    --charcoal: #262626;
    --ink: #1f1f1f;
    --rust: #c0492c;
    --note-yellow: #e8ac2e;
    --navy: #23375e;
    --text-light: #f4f4f4;
  }
  * { box-sizing: border-box; margin: 0; padding: 0; }
  html, body { width: 1200px; height: 1176px; overflow: hidden; }
  body {
    background: var(--backdrop);
    position: relative;
    font-family: "Open Sans", sans-serif;
  }
  .card {
    position: absolute;
    top: 188px;
    width: 460px;
    height: 800px;
    border-radius: 28px;
    overflow: hidden;
    background: linear-gradient(180deg, var(--card-white) 0%, var(--card-grey) 100%);
    box-shadow: 0 10px 24px rgba(0,0,0,0.22);
  }
  .card--back { left: 110px; }
  .card--front { left: 630px; }

  /* Back card */
  .back-band {
    position: absolute; left: 74px; top: 0; width: 268px; height: 100%;
    background: linear-gradient(180deg, var(--sun-yellow) 0%, var(--sun-deep) 100%);
  }
  .back-tagline {
    position: absolute; left: 74px; width: 268px; top: 215px;
    text-align: center; color: var(--ink);
  }
  .back-tagline__main {
    font-family: "Pompiere", serif; font-size: 34px; letter-spacing: 1.5px; display: block;
  }
  .back-tagline__since {
    font-family: "Cormorant SC", serif; font-size: 25px; letter-spacing: 1px; display: block; margin-top: 2px;
  }
  .back-lol {
    position: absolute; left: 74px; width: 268px; top: 315px;
    text-align: center; font-family: "Fredoka", sans-serif; font-weight: 500;
    font-size: 64px; letter-spacing: 6px; color: var(--navy);
    text-shadow: 4px 3px 0 #d9d9d9;
  }
  .back-portrait {
    position: absolute; left: 74px; top: 450px; width: 268px; height: 350px;
  }
  .back-ps {
    position: absolute; left: 22px; bottom: 40px;
    transform-origin: left bottom; transform: rotate(-90deg) translateY(22px);
    white-space: nowrap; font-family: "Pompiere", serif; font-size: 19px;
    letter-spacing: 1px; color: var(--rust);
  }

  /* Front card */
  .front-band {
    position: absolute; left: 92px; top: 250px; width: 276px; height: 528px;
    background: var(--charcoal);
  }
  .front-illustration {
    position: absolute; left: 62px; top: 40px; width: 330px; height: 220px;
  }
  .front-name {
    position: absolute; left: 92px; width: 276px; top: 272px; text-align: center;
  }
  .front-name__title {
    font-family: "Bubblegum Sans", sans-serif; font-size: 52px; color: var(--text-light); line-height: 1; display: block;
  }
  .front-name__role {
    font-family: "Oswald", sans-serif; font-weight: 600; font-size: 17px;
    color: var(--rust); letter-spacing: 0.5px; display: block; margin-top: 2px;
  }
  .front-name__note {
    font-family: "Gochi Hand", cursive; font-size: 17px; color: var(--note-yellow); display: block; margin-top: -2px;
  }
  .contact-list {
    position: absolute; left: 92px; width: 276px; top: 420px;
    list-style: none; text-align: center; color: var(--text-light);
  }
  .contact-item { margin-bottom: 12px; }
  .contact-icon { display: block; margin: 0 auto 4px; width: 16px; height: 16px; }
  .contact-value { font-size: 17px; line-height: 1.2; letter-spacing: 0.3px; display: block; }
  .contact-aside { font-size: 12.5px; line-height: 1.1; color: var(--note-yellow); display: block; }
  .network-mark { display: block; margin: 0 auto 5px; width: 13px; height: 13px; background: var(--note-yellow); }
</style>
</head>
<body>

<article class="card card--back" aria-label="Business card, back">
  <div class="back-band"></div>
  <p class="back-tagline">
    <span class="back-tagline__main">Offending people</span>
    <span class="back-tagline__since">since 1986</span>
  </p>
  <p class="back-lol">LOL</p>
  <svg class="back-portrait" role="img" aria-label="Cartoon portrait of Dane in sunglasses and a floral shirt" viewBox="0 0 268 350" preserveAspectRatio="none">
    <defs>
      <linearGradient id="portraitTone" x1="0" y1="0" x2="0" y2="1">
        <stop offset="0" stop-color="#4a2a1a"/>
        <stop offset="0.65" stop-color="#3a2418"/>
        <stop offset="1" stop-color="#23305a"/>
      </linearGradient>
    </defs>
    <rect width="268" height="350" fill="url(#portraitTone)"/>
  </svg>
  <p class="back-ps">P.S. travelling made me fatTER</p>
</article>

<article class="card card--front" aria-label="Business card, front">
  <div class="front-band"></div>
  <svg class="front-illustration" role="img" aria-label="Cartoon of Dane lounging in a yellow armchair beside a side table with a drink" viewBox="0 0 330 220" preserveAspectRatio="none">
    <defs>
      <linearGradient id="loungeTone" x1="0" y1="0" x2="1" y2="1">
        <stop offset="0" stop-color="#f0b432"/>
        <stop offset="0.6" stop-color="#e2a12b"/>
        <stop offset="1" stop-color="#c9643f"/>
      </linearGradient>
    </defs>
    <rect width="330" height="220" fill="url(#loungeTone)"/>
  </svg>

  <header class="front-name">
    <h1 class="front-name__title">Dane M.</h1>
    <span class="front-name__role">TRAVEL PHOTOGRAPHER</span>
    <span class="front-name__note">"self-proclaimed"</span>
  </header>

  <ul class="contact-list">
    <li class="contact-item">
      <svg class="contact-icon" viewBox="0 0 16 16" aria-hidden="true"><path d="M3.5 1.5l2.4 2.8-1.4 1.6c.9 2 2.4 3.5 4.4 4.5l1.6-1.4 2.8 2.4-1.5 2.3C7 13.4 2.6 9 1.3 3z" fill="var(--note-yellow)"/></svg>
      <span class="contact-value">000 000 0000</span>
      <span class="contact-aside">removing the potential awkwardness<br>of me not replying</span>
    </li>
    <li class="contact-item">
      <svg class="contact-icon" viewBox="0 0 16 16" aria-hidden="true"><rect x="1" y="3" width="14" height="10" fill="var(--note-yellow)"/><path d="M1 3l7 6 7-6" fill="none" stroke="var(--charcoal)" stroke-width="1.2"/></svg>
      <span class="contact-value">hello@dane-mail.example</span>
    </li>
    <li class="contact-item">
      <svg class="contact-icon" viewBox="0 0 16 16" aria-hidden="true" fill="none" stroke="var(--note-yellow)" stroke-width="1.1"><circle cx="8" cy="8" r="6.5"/><ellipse cx="8" cy="8" rx="3" ry="6.5"/><path d="M1.5 8h13M2.5 4.8h11M2.5 11.2h11"/></svg>
      <span class="contact-value">wanderingsofdane.example</span>
    </li>
    <li class="contact-item">
      <span class="network-mark" aria-hidden="true"></span>
      <span class="contact-value">@wanderings_of_dane</span>
    </li>
    <li class="contact-item">
      <span class="network-mark" aria-hidden="true"></span>
      <span class="contact-value">@wanderings_of_dane_2.0</span>
      <span class="contact-aside">backup for when Snapgrid puts<br>Dane on timeout for bad behaviour</span>
    </li>
  </ul>
</article>

</body>
</html>
```